Brindle Capital and Investments

Create a simple business card design using the logos attached. Make it similar but not exact to the reference photo. Brand guidelines are also included.

```html
<!DOCTYPE html>
<html lang="en">
<head>
<meta charset="utf-8">
<title>Brindle Capital – Business Card</title>
<link rel="stylesheet" href="https://fonts.googleapis.com/css2?family=Poppins:wght@400;600;700;800&display=swap">
<style>
  :root {
    --navy: #020d2e;
    --copper: #8b4210;
    --white: #ffffff;
    --paper-tint: #f1f1f3;
    --backdrop: #d3d4d6;
    --ink-soft: #1a1f36;
  }
  * { box-sizing: border-box; margin: 0; padding: 0; }
  html, body {
    width: 1200px; height: 800px; overflow: hidden;
    background: var(--backdrop);
    font-family: "Poppins", sans-serif;
  }
  .stage {
    position: relative; width: 1200px; height: 800px;
    display: flex; align-items: center; justify-content: center; gap: 40px;
  }
  .card {
    position: relative; width: 540px; height: 309px;
    background: var(--white);
    overflow: hidden;
    box-shadow: 0 14px 30px rgba(0,0,0,0.18);
  }
  /* Front */
  .card-front .pattern-field {
    position: absolute; inset: 0;
    background: linear-gradient(135deg, var(--paper-tint) 0%, var(--white) 55%, var(--paper-tint) 100%);
  }
  .card-front .front-content {
    position: absolute; inset: 0;
    display: flex; flex-direction: column; align-items: center; justify-content: center; gap: 18px;
  }
  .brand-name {
    font-weight: 800; letter-spacing: 0.08em; text-transform: uppercase;
    display: flex; align-items: center; gap: 12px;
  }
  .brand-dot {
    width: 14px; height: 14px; border-radius: 50%;
  }
  .card-front .brand-name { color: var(--navy); font-size: 34px; }
  .card-front .brand-dot { background: var(--navy); }
  .front-web { color: var(--navy); font-weight: 600; font-size: 15px; letter-spacing: 0.02em; }

  /* Back */
  .card-back { display: flex; }
  .edge-strip { width: 14px; background: var(--copper); }
  .brand-panel {
    width: 230px; background: var(--navy);
    display: flex; align-items: center; justify-content: center;
  }
  .card-back .brand-name { color: var(--white); font-size: 22px; gap: 9px; }
  .card-back .brand-dot { background: var(--white); width: 10px; height: 10px; }
  .contact-panel {
    flex: 1; padding: 62px 26px 0 30px; color: var(--ink-soft);
  }
  .person-name { font-weight: 800; font-size: 22px; color: var(--navy); letter-spacing: 0.03em; text-transform: uppercase; line-height: 1.1; }
  .person-title { font-weight: 700; font-size: 12px; color: var(--copper); letter-spacing: 0.06em; text-transform: uppercase; margin-bottom: 8px; }
  .address { font-size: 11.5px; line-height: 1.45; margin-bottom: 12px; }
  .contact-list { list-style: none; display: flex; flex-direction: column; gap: 6px; }
  .contact-item { display: flex; align-items: center; gap: 9px; font-size: 11.5px; }
  .contact-icon { width: 14px; height: 14px; flex: none; }
</style>
</head>
<body>
<main class="stage">
  <section class="card card-front">
    <div class="pattern-field" role="img" aria-label="Faint repeating monogram pattern across the card face"></div>
    <div class="front-content">
      <div class="brand-name"><span class="brand-dot"></span>Brindle Capital</div>
      <div class="front-web">www.brindlecapital.com</div>
    </div>
  </section>

  <section class="card card-back">
    <div class="edge-strip"></div>
    <div class="brand-panel">
      <div class="brand-name"><span class="brand-dot"></span>Brindle Capital</div>
    </div>
    <div class="contact-panel">
      <h1 class="person-name">Dale Horvath</h1>
      <p class="person-title">President</p>
      <p class="address">418 Ridgeline Ave,<br>Fort Worth, TX 76102</p>
      <ul class="contact-list">
        <li class="contact-item">
          <svg class="contact-icon" viewBox="0 0 24 24"><path fill="var(--copper)" d="M6.6 10.8a15 15 0 0 0 6.6 6.6l2.2-2.2a1 1 0 0 1 1-.25 11.4 11.4 0 0 0 3.6.57 1 1 0 0 1 1 1V20a1 1 0 0 1-1 1A17 17 0 0 1 3 4a1 1 0 0 1 1-1h3.5a1 1 0 0 1 1 1c0 1.25.2 2.45.57 3.57a1 1 0 0 1-.25 1z"/></svg>
          (888) 555-0147
        </li>
        <li class="contact-item">
          <svg class="contact-icon" viewBox="0 0 24 24"><path fill="var(--copper)" d="M2 5h20v14H2z"/><path fill="none" stroke="var(--white)" stroke-width="1.8" d="M2.5 5.5 12 13l9.5-7.5"/></svg>
          hello@brindlecapital.com
        </li>
        <li class="contact-item">
          <svg class="contact-icon" viewBox="0 0 24 24" fill="none" stroke="var(--copper)" stroke-width="2"><circle cx="12" cy="12" r="9"/><path d="M3 12h18M12 3c3 3.5 3 14.5 0 18M12 3c-3 3.5-3 14.5 0 18"/></svg>
          www.brindlecapital.com
        </li>
      </ul>
    </div>
  </section>
</main>
</body>
</html>
```